New wine label design aimed at millennials

We have developed 2 new quality wines - a crisp, cool climate Chardonnay from the Orange region and a spicy Shiraz from the Gundagai wine region.

Each of these wines have been made in a distinctly modern style, with less oak and more elegance than most and come from two relatively new but exciting wine regions.

They are distinctly food friendly as a result.

These are classic varieties, with a modern take from 'undiscovered' regions.

We are seeking to target millennial wine drinkers who are possibly new to wine or are early in their journey into wine.

We are after a contemporary single label design (i.e. - not a font ab back label) to be applied to a 'lean green' burgundy bottle that speaks to the modern take on classic varieties from undiscovered regions.

We have already recieved a umber of good designs based on some possible brand names:

Tessaly
Copper and Quill
The Velvet Almanac

And now we would like to purse labels focusing just on Copper and Quill (of course if a bolt of lightening strikes you on the other names, feel free!)

the reference to Copper and Quill comes from a story attached to one of our existing labels – Marion Treloar. The two Treloar brothers who founded this Vineyard famously borrowed a Copper and Quill from a well-established winery family in order for them to roam the local foothills in order to find their ideal vineyard site.

We would like to capture this sense of exploration and discovery in what would form a sub-tier label for this brand.

It would still be targeting very much millennial's and so we want the label to look contemporary and urban, but reflect the sense of exploration and discovery awhile referencing the historical authenticity of the whole overarching brand structure.

I have attached a number of inspirational images that would need to be translated into a more modern visual setting.

obviously use of a horse and a matter in some sort of "branded" image would be a first step and obviously the historical/authentic back story combined with a modern anaesthetic lends itself to plain black-and-white.

However, clever use of a modern colour palette would also be very welcome.
Updates

For further inspiration we have been considering the following phrases and words as possible label namesGallivant - giving a sense of freewheeling adventure and explorationHorse & Mattock - referencing an old story of 2 pioneer vignerons being lent a horse and a mattock to go out and find their ideal vineyard sites, introducing concepts of innovation, discovery and authenticityThe Gentleman Vigneron - referencing a founding winemakers nominal descriptor of himself and bringing a true element of authenticity and quality. Added Monday, July 31, 2017

Project Deadline Extended Reason: I am hoping to give some more information and focus on the desired outcomes.The name of the label will be Copper and Quill.Please review the prior comments to get the background on this and I will add more information as well.I will try to identify and provide some other design work that aligns with what we are trying to achieve also. Added Friday, August 11, 2017

Target Market(s)

Millennials, skewing female 21-35 years, university educated, employed in white collar or professional industry, urban

Font styles to use
Serif
Sans Serif

Colors

Designer to choose colors to be used in the design.

Requirements
Must have
• Modern, contemporary urban look and feel that stands out on the shelf.
• Must be relevant and attractive to millennials.
• Sense of humour or quirkiness to it.
• We like this label amongst many other
• http://www.pellbrookcellars.com/shopwines/
Nice to have
• We will aim to use recycled/low carbon footprint glass in the packaging (i.e. the lean green bottles) so would also aim to use 100% recycled paper on the label and would like to mention this in the design.

```html
<!DOCTYPE html>
<html lang="en">
<head>
<meta charset="utf-8">
<title>Tessaly Chardonnay – Label Variants</title>
<link rel="stylesheet" href="https://fonts.googleapis.com/css2?family=Archivo+Black&family=Source+Sans+3:wght@400;600;700&display=swap">
<style>
  :root {
    --canvas: #ffffff;
    --label-dark: #333333;
    --label-light: #ffffff;
    --frame: #d9502a;
    --accent: #e05a2b;
    --brand-green: #2e6b34;
    --volume-green: #3c7a45;
    --art-pink: #f2b8a8;
    --art-teal: #6cc9d6;
    --art-mint: #b9e0cf;
  }
  * { box-sizing: border-box; margin: 0; padding: 0; }
  html, body {
    width: 1200px;
    height: 848px;
    overflow: hidden;
    background: var(--canvas);
  }
  .canvas {
    position: relative;
    width: 1200px;
    height: 848px;
    display: flex;
    justify-content: center;
    align-items: center;
    gap: 26px;
  }
  .label {
    position: relative;
    width: 440px;
    height: 656px;
    border: 2px solid var(--frame);
    font-family: "Source Sans 3", "Helvetica Neue", Arial, sans-serif;
  }
  .label--dark { background: var(--label-dark); }
  .label--light {
    background: var(--label-light);
    box-shadow: 2px 3px 5px rgba(0,0,0,0.18);
  }
  .label__art {
    position: absolute;
    left: 34px;
    top: 40px;
    width: 340px;
    height: 410px;
    border-radius: 46% 54% 40% 60% / 40% 38% 62% 60%;
    background:
      radial-gradient(circle at 40% 22%, var(--art-pink) 0 22%, transparent 46%),
      radial-gradient(circle at 78% 40%, var(--art-teal) 0 18%, transparent 42%),
      radial-gradient(circle at 35% 68%, var(--art-mint) 0 30%, transparent 60%),
      linear-gradient(160deg, var(--art-pink), var(--art-mint) 55%, var(--art-teal));
    opacity: 0.9;
  }
  .label__tagline {
    position: absolute;
    right: 40px;
    top: 358px;
    text-align: center;
    color: var(--accent);
    line-height: 1.1;
  }
  .label__tagline-top {
    display: block;
    font-size: 23px;
    font-weight: 400;
  }
  .label__tagline-region {
    display: block;
    font-size: 25px;
    font-weight: 700;
  }
  .label__brand {
    position: absolute;
    left: 0;
    right: 0;
    top: 462px;
    text-align: center;
    font-family: "Archivo Black", "Arial Black", sans-serif;
    font-size: 58px;
    letter-spacing: -0.5px;
    color: var(--brand-green);
    line-height: 1;
  }
  .label__variety {
    position: absolute;
    left: 0;
    right: 0;
    top: 565px;
    text-align: center;
    font-size: 22px;
    font-weight: 700;
    letter-spacing: 0.36em;
    padding-left: 0.36em;
    color: var(--accent);
  }
  .label__volume {
    position: absolute;
    left: 0;
    right: 0;
    top: 610px;
    text-align: center;
    font-size: 18px;
    letter-spacing: 0.18em;
    padding-left: 0.18em;
    color: var(--volume-green);
  }
  .label--dark .label__volume { color: var(--accent); }
</style>
</head>
<body>
  <main class="canvas">
    <section class="label label--dark" aria-label="Tessaly Chardonnay label, dark variant">
      <div class="label__art" role="img" aria-label="Multicoloured illustration of a rearing horse in pink, mint and teal"></div>
      <p class="label__tagline">
        <span class="label__tagline-top">CRISP &amp; COOL</span>
        <span class="label__tagline-region">Orange Region</span>
      </p>
      <h1 class="label__brand">TESSALY</h1>
      <p class="label__variety">CHARDONNAY</p>
      <p class="label__volume">750ml</p>
    </section>

    <section class="label label--light" aria-label="Tessaly Chardonnay label, light variant">
      <div class="label__art" role="img" aria-label="Multicoloured illustration of a rearing horse in pink, mint and teal"></div>
      <p class="label__tagline">
        <span class="label__tagline-top">CRISP &amp; COOL</span>
        <span class="label__tagline-region">Orange Region</span>
      </p>
      <h2 class="label__brand">TESSALY</h2>
      <p class="label__variety">CHARDONNAY</p>
      <p class="label__volume">750ml</p>
    </section>
  </main>
</body>
</html>
```